Women's Online Clothing Boutique Needs Business Cards

I already have a logo that I would like to use. Some of the things that interest me is black business cards, foil embossed logo, glossy embossed logo, leopard print, no yellow font, rounded edges. I even like just a large logo on the front side with all of my information on the back side.

Contact Information for Business Card

https://silverheron.shopvenlo.com/
https://www.pagelink.net/thesilverheronboutique/
https://www.picfeed.net/thesilverheronboutique/
silverheronboutique@mailora.net

Requirements
Must have
• My Logo
Nice to have
• Leopard Print
Should not have
• No Yellow Font

```html
<!DOCTYPE html>
<html lang="en">
<head>
<meta charset="utf-8">
<title>The Silver Heron Boutique — Business Cards</title>
<link href="https://fonts.googleapis.com/css2?family=Roboto:wght@400;500;700&display=swap" rel="stylesheet">
<style>
  :root {
    --backdrop: #d9dcdd;
    --card-light: #f4f3ef;
    --card-dark: #1d1d1e;
    --gold-edge: #c9a13a;
    --rule: #8a8a8a;
    --ink: #2a2a2a;
    --ink-soft: #4a4a4a;
    --silver: #9a9a9c;
  }
  * { margin: 0; padding: 0; box-sizing: border-box; }
  html, body { width: 1200px; height: 754px; overflow: hidden; }
  body {
    background: var(--backdrop);
    font-family: "Roboto", Arial, sans-serif;
    display: flex;
    align-items: center;
    justify-content: center;
    gap: 40px;
  }
  .card {
    width: 540px;
    height: 309px;
    border-radius: 4px;
    box-shadow: 0 10px 24px rgba(0,0,0,.18);
    position: relative;
  }
  .card-front {
    background: var(--card-light);
    display: flex;
    align-items: center;
    padding: 0 30px;
  }
  .card-back {
    background: var(--card-dark);
    border-bottom: 4px solid var(--gold-edge);
    display: flex;
    align-items: center;
    justify-content: center;
  }
  .brand {
    display: flex;
    align-items: center;
    gap: 10px;
    font-weight: 500;
  }
  .brand-dot {
    width: 14px; height: 14px; border-radius: 50%;
    background: currentColor;
    flex: none;
  }
  .brand-name { line-height: 1.15; }
  .card-front .brand {
    color: var(--ink);
    width: 180px;
    font-size: 22px;
    flex: none;
  }
  .card-back .brand {
    color: var(--silver);
    font-size: 40px;
  }
  .divider {
    width: 1.5px;
    height: 150px;
    background: var(--rule);
    margin: 0 20px 0 16px;
    flex: none;
  }
  .contact { color: var(--ink); font-size: 13px; line-height: 1.45; white-space: nowrap; }
  .contact-name {
    color: var(--ink);
    font-weight: 700;
    font-size: 15px;
    letter-spacing: .5px;
    text-transform: uppercase;
  }
  .contact-title { font-weight: 500; color: var(--ink-soft); margin-bottom: 8px; }
  .contact-address { margin-bottom: 8px; }
  .contact-row { display: flex; align-items: center; gap: 7px; }
  .contact-row svg { width: 12px; height: 12px; flex: none; fill: var(--ink-soft); }
</style>
</head>
<body>
  <section class="card card-front">
    <div class="brand">
      <span class="brand-dot"></span>
      <span class="brand-name">The Silver Heron Boutique</span>
    </div>
    <div class="divider"></div>
    <div class="contact">
      <p class="contact-name">Marcus Ellery</p>
      <p class="contact-title">Managing Director</p>
      <p class="contact-address">4127 N. Larkspur Ave,<br>Mesa Ridge, AZ 85990</p>
      <p class="contact-row">
        <svg viewBox="0 0 24 24" aria-hidden="true"><path d="M6.6 10.8a15 15 0 0 0 6.6 6.6l2.2-2.2c.3-.3.7-.4 1-.2 1.1.4 2.3.6 3.6.6.6 0 1 .4 1 1V20c0 .6-.4 1-1 1A17 17 0 0 1 3 4c0-.6.4-1 1-1h3.5c.6 0 1 .4 1 1 0 1.3.2 2.5.6 3.6.1.3 0 .7-.2 1z"/></svg>
        555-014-2290
      </p>
      <p class="contact-row">
        <svg viewBox="0 0 24 24" aria-hidden="true"><path d="M2 5h20v14H2zm2 2v.5l8 5 8-5V7l-8 5z"/></svg>
        silverheronboutique@mailora.net
      </p>
      <p class="contact-row">
        <svg viewBox="0 0 24 24" aria-hidden="true"><circle cx="12" cy="12" r="10"/></svg>
        silverheron.shopvenlo.com
      </p>
    </div>
  </section>

  <section class="card card-back">
    <div class="brand">
      <span class="brand-dot"></span>
      <span class="brand-name">The Silver Heron Boutique</span>
    </div>
  </section>
</body>
</html>
```